Law firm Seeks Modern and Engaging Site Redesign

Law firm seeks a new web site. Should be modern, but retaining existing logo. Needs to include contact section, professional bio, services offered, and contact information.

The site should be modern, responsive, and able to be SEO optimized.

The finished product should be coded in a Wordpress site, which I will provide. I can work with other platforms, including Wix, but WP is preferred.

Note the current site is https://www.tallowfieldlaw.example/#/home

Target Market(s)

Family Law Practice

Industry/Entity Type

Legal

Coding

Coded - Design and coding required

Number of Pages Required

4 page

Font styles to use
Sans Serif

Requirements
Must have
• Service description
Bio pages for partners
Contact Form
Awards/Publication page

```html
<!DOCTYPE html>
<html lang="en">
<head>
<meta charset="utf-8">
<title>Tallowfield | Reyes — Law Firm</title>
<link href="https://fonts.googleapis.com/css2?family=Montserrat:wght@400;500;600;700;800&family=Open+Sans:ital,wght@0,400;0,600;1,400&display=swap" rel="stylesheet">
<style>
:root{
  --navy:#1c2763;
  --blue:#2c3c8e;
  --blue-mid:#3b4fb0;
  --btn:#4a67e0;
  --red:#d9473b;
  --ink:#1e2235;
  --muted:#6b7080;
  --light:#eef0f6;
  --line:#d9dce6;
  --white:#ffffff;
}
*{box-sizing:border-box;margin:0;padding:0}
html,body{width:1200px;height:3904px;overflow:hidden}
body{font-family:"Open Sans",Arial,sans-serif;color:var(--ink);background:var(--white);position:relative}
h1,h2,h3,h4,.mont{font-family:"Montserrat",Arial,sans-serif}
section{position:relative;width:1200px;overflow:hidden}
.eyebrow{font-family:"Montserrat",Arial,sans-serif;font-size:11px;font-weight:600;letter-spacing:1.5px;text-transform:uppercase;color:var(--muted)}
.read-more{font-family:"Montserrat",Arial,sans-serif;font-size:11px;font-weight:700;color:var(--red);letter-spacing:1px;text-transform:uppercase}
.btn{display:inline-block;background:var(--btn);color:var(--white);font-family:"Montserrat",Arial,sans-serif;font-size:11px;font-weight:700;letter-spacing:1px;text-transform:uppercase;padding:12px 24px;border-radius:3px}

/* hero */
.hero{height:552px;background:linear-gradient(135deg,#2b3a86 0%,#1f2a6b 60%,#17205a 100%)}
.hero-photo{position:absolute;inset:0;background:linear-gradient(90deg,rgba(60,80,170,.35),rgba(30,40,110,.1) 50%,rgba(70,90,180,.3));}
.nav{position:absolute;top:0;left:0;right:0;height:72px;display:flex;align-items:center;padding:0 225px;justify-content:space-between}
.logo{font-family:"Montserrat",Arial,sans-serif;font-weight:600;font-size:20px;color:var(--white);display:flex;align-items:center;gap:10px}
.logo-box{width:14px;height:14px;background:var(--white)}
.nav-links{display:flex;gap:22px;font-family:"Montserrat",Arial,sans-serif;font-size:10px;font-weight:600;color:var(--white);text-transform:uppercase;letter-spacing:.8px}
.hero-text{position:absolute;left:225px;top:235px;color:var(--white)}
.hero-text h1{font-size:44px;font-weight:700;line-height:1.12}
.hero-text p{font-size:12px;line-height:1.6;margin:14px 0 20px;color:#d4d9f2;max-width:330px}
.hero-dots{position:absolute;left:955px;top:260px;display:flex;flex-direction:column;gap:10px}
.hero-dots span{width:7px;height:7px;border-radius:50%;background:rgba(255,255,255,.45)}
.hero-dots span.on{background:var(--white)}

/* about */
.about{height:296px;text-align:center;padding-top:56px}
.about h2{font-size:28px;font-weight:700;color:var(--ink);line-height:1.25;margin-top:8px}
.about p{font-size:12px;color:var(--muted);line-height:1.7;width:560px;margin:16px auto 18px}

/* partners photo band */
.partners{height:360px;background:linear-gradient(180deg,#fff 0,#fff 60%,#e6e9f2 60%)}
.partners-photo{position:absolute;left:260px;top:0;width:680px;height:360px;background:linear-gradient(180deg,#d3d5db,#b9bcc5 70%,#a3a7b3)}

/* practice */
.practice{height:312px;background:linear-gradient(180deg,#e6e9f2,#eceef5)}
.practice-intro{position:absolute;left:225px;top:60px;width:200px}
.practice-intro h2{font-size:26px;font-weight:700;line-height:1.2;color:var(--blue);margin:6px 0 12px}
.practice-intro p{font-size:11px;color:var(--muted);line-height:1.6;margin-bottom:14px}
.practice-grid{position:absolute;left:460px;top:-10px;display:grid;grid-template-columns:repeat(3,160px);gap:16px}
.card{background:var(--white);height:140px;padding:18px 16px;box-shadow:0 6px 18px rgba(30,40,100,.08);position:relative}
.card svg{display:block;margin-bottom:10px}
.card h4{font-size:13px;font-weight:600;color:var(--ink);line-height:1.3}
.card .read-more{position:absolute;left:16px;bottom:16px}
.card.featured{background:var(--navy);color:var(--white)}
.card.featured h4{color:var(--white)}
.card.featured p{font-size:10px;line-height:1.5;color:#c8cdea;margin-top:6px}

/* advice */
.advice{height:560px;background:linear-gradient(180deg,#2e3f95,#26347f);text-align:center;color:var(--white);padding-top:90px}
.advice h2{font-size:30px;font-weight:700;margin:14px 0 12px}
.advice p{font-size:15px;line-height:1.6;font-family:"Montserrat",Arial,sans-serif;color:#e1e5f7}
.advice .phone{font-size:22px;font-weight:700;margin-top:8px;font-family:"Montserrat",Arial,sans-serif}
.stats{display:flex;justify-content:center;gap:52px;margin-top:50px}
.stat{width:122px;height:122px;border-radius:50%;background:var(--navy);display:flex;flex-direction:column;align-items:center;justify-content:center}
.stat b{font-family:"Montserrat",Arial,sans-serif;font-size:30px;font-weight:700}
.stat span{font-size:10px;color:#c8cdea;margin-top:2px}

/* attorneys */
.attorneys{height:420px;text-align:center;padding-top:60px}
.attorneys h2{font-size:28px;font-weight:700;color:var(--ink);margin:6px 0 26px}
.team{display:flex;justify-content:center;gap:20px}
.member{width:172px}
.member-photo{height:150px;background:linear-gradient(180deg,#d9dbe0,#9fa3ad)}
.member h4{font-size:11px;font-weight:600;margin-top:12px}
.member small{display:block;font-size:9px;color:var(--muted);margin:3px 0 8px}

/* testimonials */
.testimonials{height:320px;background:linear-gradient(180deg,#f1f2f6,#e4e6ee);text-align:center;padding-top:60px}
.testimonials h2{font-size:28px;font-weight:700;color:var(--blue);margin:6px 0 14px}
.quote-mark{font-family:"Montserrat",Arial,sans-serif;font-size:54px;color:#b8bccb;line-height:.8;height:36px}
.testimonials blockquote{font-style:italic;font-size:16px;line-height:1.55;color:var(--blue);width:560px;margin:6px auto 10px}
.testimonials cite{font-size:10px;color:var(--muted);font-style:normal}

/* blog */
.blog{height:500px;text-align:center;padding-top:50px}
.blog h2{font-size:28px;font-weight:700;margin:6px 0 30px}
.posts{display:flex;justify-content:center;gap:24px;text-align:left}
.post{width:220px}
.post-photo{height:142px;background:linear-gradient(135deg,#6b4c3b,#a8896f)}
.post-photo.b{background:linear-gradient(135deg,#8a8f99,#d3d5da)}
.post-photo.c{background:linear-gradient(135deg,#2f3547,#7c8091)}
.post time{display:block;font-size:9px;color:var(--muted);margin:14px 0 4px}
.post h4{font-size:13px;font-weight:700}
.post p{font-size:10px;line-height:1.6;color:var(--muted);margin:6px 0 10px}

/* contact */
.contact{height:540px;background:linear-gradient(180deg,#2b3b8c,#243277);color:var(--white)}
.contact-info{position:absolute;left:232px;top:110px;width:280px}
.contact-info .eyebrow{color:#b9c0e6}
.contact-info h2{font-size:26px;font-weight:700;line-height:1.25;margin:10px 0 20px}
.contact-info p{font-size:11px;line-height:1.8;color:#d5daf3;margin-bottom:22px}
.form{position:absolute;left:580px;top:40px;width:400px;height:460px;background:var(--white);padding:32px 26px;color:var(--ink)}
.row{display:flex;gap:16px;margin-bottom:18px}
.field{flex:1}
.field label{display:block;font-size:10px;font-weight:600;margin-bottom:6px}
.field .input{height:32px;border:1px solid var(--line)}
.field .textarea{height:110px;border:1px solid var(--line)}
.form .btn{margin-top:8px}

/* footer */
.footer{height:44px;background:var(--navy);display:flex;align-items:center;justify-content:space-between;padding:0 225px;color:#aab2dc;font-size:10px}
.social{display:flex;gap:12px}
.social span{width:10px;height:10px;border-radius:50%;background:#aab2dc}
</style>
</head>
<body>

<section class="hero">
  <div class="hero-photo" role="img" aria-label="Classical courthouse columns in deep blue tones"></div>
  <nav class="nav">
    <div class="logo"><span class="logo-box"></span>Tallowfield | Reyes</div>
    <div class="nav-links"><span>Home</span><span>About</span><span>Practice Areas</span><span>Attorneys</span><span>Blog</span><span>Contact</span></div>
    <span class="btn">Free Consultation</span>
  </nav>
  <div class="hero-text">
    <h1>Get the Best<br>Reliable Legal Solutions</h1>
    <p>With over 30 years of experience, we guide families through every legal step with care and clear advice.</p>
    <span class="btn">Read More</span>
  </div>
  <div class="hero-dots"><span class="on"></span><span></span><span></span></div>
</section>

<section class="about">
  <div class="eyebrow">Who We Are</div>
  <h2>We Are the Best Law Firm<br>in New Jersey</h2>
  <p>The law firm of Tallowfield &amp; Reyes LLC is located in Hackensack, serving clients across New Jersey. Our attorneys handle family law, divorce, criminal defense, municipal court, real estate and wills with dedication, honesty and personal attention to every single client.</p>
  <span class="read-more">Read More</span>
</section>

<section class="partners">
  <div class="partners-photo" role="img" aria-label="Two partners of the firm standing in the office in dark suits"></div>
</section>

<section class="practice">
  <div class="practice-intro">
    <div class="eyebrow">Our Services</div>
    <h2>Our Legal<br>Practice Areas</h2>
    <p>We offer focused legal help across several practice areas, always with clear advice and steady support.</p>
    <span class="read-more">View All Services</span>
  </div>
  <div class="practice-grid">
    <div class="card">
      <svg width="26" height="26" viewBox="0 0 26 26" fill="none" stroke="#4a67e0" stroke-width="1.6"><path d="M4 22h18M7 22V12M13 22V12M19 22V12M3 10l10-6 10 6z"/></svg>
      <h4>Criminal<br>Practice</h4><span class="read-more">More</span>
    </div>
    <div class="card featured">
      <h4>Family Law/<br>Divorce</h4>
      <p>Careful guidance on divorce, custody, support and every family matter you face.</p>
    </div>
    <div class="card">
      <svg width="26" height="26" viewBox="0 0 26 26" fill="none" stroke="#4a67e0" stroke-width="1.6"><circle cx="13" cy="8" r="4"/><path d="M5 23c0-5 4-8 8-8s8 3 8 8"/></svg>
      <h4>Juvenile<br>Practice</h4><span class="read-more">More</span>
    </div>
    <div class="card">
      <svg width="26" height="26" viewBox="0 0 26 26" fill="none" stroke="#4a67e0" stroke-width="1.6"><rect x="4" y="10" width="18" height="12"/><path d="M2 10l11-7 11 7M9 22v-6h8v6"/></svg>
      <h4>Municipal<br>Court</h4><span class="read-more">More</span>
    </div>
    <div class="card">
      <svg width="26" height="26" viewBox="0 0 26 26" fill="none" stroke="#4a67e0" stroke-width="1.6"><path d="M3 13L13 4l10 9M6 11v11h14V11"/><rect x="11" y="15" width="4" height="7"/></svg>
      <h4>Real<br>Estate</h4><span class="read-more">More</span>
    </div>
    <div class="card">
      <svg width="26" height="26" viewBox="0 0 26 26" fill="none" stroke="#4a67e0" stroke-width="1.6"><path d="M6 3h10l5 5v15H6z"/><path d="M9 12h9M9 16h9M9 20h6"/></svg>
      <h4>Wills/Trusts</h4><span class="read-more">More</span>
    </div>
  </div>
</section>

<section class="advice">
  <svg width="44" height="40" viewBox="0 0 44 40" fill="none" stroke="#ffffff" stroke-width="2"><path d="M4 14L22 4l18 10zM8 14v18M16 14v18M28 14v18M36 14v18M3 34h38M2 38h40"/></svg>
  <h2>Need Legal Advice?</h2>
  <p>To Discuss Your Matter With Either Mr. Tallowfield or Mr. Reyes Send Us<br>Your Details About Your Situation or Contact Us Directly At</p>
  <div class="phone">(201) 555-0148</div>
  <div class="stats">
    <div class="stat"><b>1350</b><span>Satisfied Clients</span></div>
    <div class="stat"><b>30+</b><span>Years of Experience</span></div>
    <div class="stat"><b>478</b><span>Total Case Won</span></div>
    <div class="stat"><b>17</b><span>Awards &amp; Honors</span></div>
  </div>
</section>

<section class="attorneys">
  <div class="eyebrow">Most Professional Team</div>
  <h2>Meet Our Attorneys</h2>
  <div class="team">
    <div class="member"><div class="member-photo" role="img" aria-label="Portrait of attorney Martin L. Tallowfield"></div><h4>Martin L. Tallowfield, Esq.</h4><small>Founding Partner</small><span class="read-more">View Profile</span></div>
    <div class="member"><div class="member-photo" role="img" aria-label="Portrait of attorney Daniel R. Reyes"></div><h4>Daniel R. Reyes, Esq.</h4><small>Managing Partner</small><span class="read-more">View Profile</span></div>
    <div class="member"><div class="member-photo" role="img" aria-label="Portrait of attorney Clara V. Osterby"></div><h4>Clara V. Osterby, Esq.</h4><small>Associate Attorney</small><span class="read-more">View Profile</span></div>
    <div class="member"><div class="member-photo" role="img" aria-label="Portrait of attorney Peter J. Haldane"></div><h4>Peter J. Haldane, Esq.</h4><small>Of Counsel</small><span class="read-more">View Profile</span></div>
  </div>
</section>

<section class="testimonials">
  <div class="eyebrow">Moments to Cherish</div>
  <h2>Satisfied Clients Stories</h2>
  <div class="quote-mark">&ldquo;</div>
  <blockquote>Lorem ipsum dolor sit amet, consectetur adipiscing elit, sed do eiusmod tempor incididunt ut labore et dolore magna aliqua. Quis ipsum suspendisse ultrices gravida. Risus commodo viverra maecenas accumsan.</blockquote>
  <cite>Laura Glen — Client</cite>
</section>

<section class="blog">
  <div class="eyebrow">Our Blog</div>
  <h2>Find Out About Activities</h2>
  <div class="posts">
    <div class="post"><div class="post-photo" role="img" aria-label="Judge's gavel on a wooden desk"></div><time>May 18, 2020</time><h4>Law and Order</h4><p>A short look at how local courts handle family disputes and what to expect.</p><span class="read-more">Read More</span></div>
    <div class="post"><div class="post-photo b" role="img" aria-label="Hands signing legal documents"></div><time>May 12, 2020</time><h4>Time for Action</h4><p>Simple steps to prepare your paperwork before meeting with your attorney.</p><span class="read-more">Read More</span></div>
    <div class="post"><div class="post-photo c" role="img" aria-label="Lawyer in a suit at the office"></div><time>May 04, 2020</time><h4>Lawyer Lifestyle</h4><p>Inside a working day at our office and how our team serves each client.</p><span class="read-more">Read More</span></div>
  </div>
</section>

<section class="contact">
  <div class="contact-info">
    <div class="eyebrow">Get in Touch</div>
    <h2>Are You Having any<br>Problems?<br>Talk to Us!</h2>
    <p>Tallowfield &amp; Reyes LLC<br>14 Linden Court, Suite 200<br>Hackensack, NJ 07601<br>Phone: (201) 555-0148<br>Fax: (201) 555-0149</p>
    <span class="btn">Get Directions</span>
  </div>
  <div class="form">
    <div class="row"><div class="field"><label>First Name</label><div class="input"></div></div><div class="field"><label>Last Name</label><div class="input"></div></div></div>
    <div class="row"><div class="field"><label>Email</label><div class="input"></div></div><div class="field"><label>Practice Area</label><div class="input"></div></div></div>
    <div class="row"><div class="field"><label>Message</label><div class="textarea"></div></div></div>
    <span class="btn">Send Message</span>
  </div>
</section>

<footer class="footer">
  <span>© 2020 Tallowfield &amp; Reyes LLC | Privacy Policy</span>
  <div class="social"><span></span><span></span><span></span></div>
</footer>

</body>
</html>
```